Business Card

I would like a business card with a picture of my husband and I that is unique and professional.

Industry/Entity Type

Business

Font styles to use
Serif

```html
<!DOCTYPE html>
<html lang="en">
<head>
<meta charset="utf-8">
<title>Brooks Leadership Development – Business Card</title>
<link rel="stylesheet" href="https://fonts.googleapis.com/css2?family=Cinzel:wght@400;600&family=Signika:wght@600&family=Tinos&display=swap">
<style>
  :root {
    --page-bg: #ece7df;
    --card-shadow: rgba(0,0,0,0.35);
    --back-top: #8d8a80;
    --back-mid: #a0907a;
    --back-bottom: #8a887f;
    --ink-white: #ffffff;
    --gold: #f2b01e;
    --band: rgba(255,255,255,0.16);
    --photo-light: #f6eef6;
    --photo-hair: #2a1d1a;
    --photo-suit: #8a8a8c;
    --photo-skin: #b07a5c;
  }
  * { margin: 0; padding: 0; box-sizing: border-box; }
  html, body { width: 1200px; height: 914px; overflow: hidden; }
  body { background: var(--page-bg); position: relative; }

  .card {
    position: absolute;
    top: 65px;
    width: 417px;
    height: 713px;
    box-shadow: 0 4px 14px var(--card-shadow);
    overflow: hidden;
  }
  .card--front { left: 100px; }
  .card--back  { left: 666px; }

  .couple-photo {
    width: 100%; height: 100%;
    background:
      radial-gradient(ellipse 35% 22% at 45% 18%, var(--photo-hair) 0 60%, transparent 100%),
      radial-gradient(ellipse 30% 18% at 48% 30%, var(--photo-skin) 0 55%, transparent 100%),
      radial-gradient(ellipse 32% 20% at 72% 68%, var(--photo-skin) 0 55%, transparent 100%),
      linear-gradient(180deg, var(--photo-light) 0%, var(--photo-light) 30%, var(--photo-suit) 70%, #5e5d60 100%);
  }

  .card--back {
    background:
      radial-gradient(ellipse 70% 45% at 50% 45%, var(--back-mid), transparent 80%),
      linear-gradient(180deg, var(--back-top), var(--back-bottom));
    color: var(--ink-white);
    text-align: center;
  }
  .holder-name {
    position: absolute; top: 32px; left: 0; right: 0;
    font-family: "Cinzel", serif;
    font-weight: 600;
    font-size: 38px;
    letter-spacing: 2px;
  }
  .holder-title {
    position: absolute; top: 96px; left: 0; right: 0;
    font-family: "Signika", sans-serif;
    font-weight: 600;
    font-size: 24px;
    line-height: 36px;
    color: var(--gold);
    text-shadow: 0 1px 2px rgba(0,0,0,0.4);
  }
  .brand-mark {
    position: absolute; top: 240px; left: 0; right: 0;
    display: flex; flex-direction: column; align-items: center; gap: 14px;
  }
  .brand-mark__dot {
    width: 70px; height: 70px; border-radius: 50%;
    background: var(--gold);
  }
  .brand-mark__name {
    font-family: "Cinzel", serif;
    font-weight: 600;
    font-size: 44px;
    color: var(--gold);
  }
  .company {
    position: absolute; top: 462px; left: 0; right: 0;
    font-family: "Cinzel", serif;
    font-size: 18.5px;
    letter-spacing: 0.5px;
  }
  .company-rule { position: absolute; top: 484px; left: 16px; }
  .contact-band {
    position: absolute; top: 550px; left: 0; right: 0; bottom: 0;
    background: var(--band);
  }
  .phone {
    position: absolute; top: 572px; left: 0; right: 0;
    display: flex; justify-content: center; align-items: center; gap: 10px;
    font-family: "Tinos", serif;
    font-size: 41px;
  }
  .email {
    position: absolute; top: 640px; left: 0; right: 0;
    display: flex; justify-content: center; align-items: center; gap: 14px;
    font-family: "Signika", sans-serif;
    font-weight: 600;
    font-size: 21px;
  }
</style>
</head>
<body>
  <section class="card card--front">
    <div class="couple-photo" role="img" aria-label="Portrait photograph of the couple, smiling, in grey suits against a light backdrop"></div>
  </section>

  <section class="card card--back">
    <h1 class="holder-name">Nadia Brooks</h1>
    <p class="holder-title">Professitonal Mentorship<br>Strategist</p>

    <div class="brand-mark">
      <span class="brand-mark__dot"></span>
      <span class="brand-mark__name">Brooks</span>
    </div>

    <p class="company">Brooks Leadership Development</p>
    <svg class="company-rule" width="385" height="24" viewBox="0 0 385 24" aria-hidden="true">
      <g stroke="#ffffff" stroke-width="1.3" fill="none">
        <line x1="4" y1="6" x2="381" y2="6"/>
        <path d="M4 6 l8 -4 M4 6 l8 4 M12 6 l-4 -4 M12 6 l-4 4"/>
        <path d="M381 6 l-8 -4 M381 6 l-8 4 M373 6 l4 -4 M373 6 l4 4"/>
        <path d="M192.5 13 v8 M188.5 17 h8"/>
      </g>
    </svg>

    <div class="contact-band"></div>
    <p class="phone">
      <svg width="26" height="32" viewBox="0 0 26 32" aria-hidden="true">
        <path fill="#111" d="M6 2 l5 1 2 8 -4 3 c2 5 4 8 8 11 l4 -3 6 4 -1 5 c-2 1 -5 1 -7 0 C9 27 3 18 1 9 c0 -3 2 -6 5 -7z"/>
      </svg>
      <span>555-014-2290</span>
    </p>
    <p class="email">
      <svg width="20" height="14" viewBox="0 0 20 14" aria-hidden="true">
        <rect width="20" height="14" fill="#111"/>
        <path d="M0 0 L10 8 L20 0" stroke="#888" stroke-width="1.2" fill="none"/>
      </svg>
      <span>NadiaBrooks@example.com</span>
    </p>
  </section>
</body>
</html>
```